Crestline Ridge Alloys Website

I need a redesign of my current website: www.crestlineridgealloys.example.
I would like to update the look, add some new stock photos of shiny stainless steel bar stock items. All of our grades of material should show on each page so that when people search for the grades on Google, our company site comes up. Most of the text content will be the same with some more changes. Also, we will want to add a button for calling our company for sales calls and one for sending a request for quote. I want the graphics to get prospects attention. I won't people to see us as a large stocking facility that is strong. Bold colors, silver, red, and blue.

Target Market(s)

Contract manufacturers, screw machine houses, medical instrument manufacturers, oil and gas parts industry, aerospace industry, automotive industry, food industry

Number of Pages Required

5+ page

Font styles to use
Sans Serif

Colors
ec1f27
0355a3

Requirements
Must have
• Pictures of stainless steel round bar. Also, a button linking someone to sales@crestlineridgealloys.example and our phone # 612-735-2048. Main stainless steel and titanium grades listed on each and every page. Also, a 1 page copy of our ISO 9001 certificatation.

```html
<!DOCTYPE html>
<html lang="en">
<head>
<meta charset="utf-8">
<title>Contact – Crestline Ridge Alloys</title>
<link href="https://fonts.googleapis.com/css2?family=Arimo:wght@400;700&family=Open+Sans:wght@400&family=Quicksand:wght@300;400;500&display=swap" rel="stylesheet">
<style>
:root{
  --blue:#0355a3;
  --red:#ec1f27;
  --topbar:#2a2a2c;
  --page:#efefef;
  --text:#555;
  --muted:#999;
  --field:#f3f3f3;
  --field-border:#c9c9c9;
  --footer:#262626;
  --footer-bottom:#1b1b1b;
  --footer-text:#8d8d8d;
}
*{margin:0;padding:0;box-sizing:border-box}
html,body{width:1120px;height:1200px;overflow:hidden}
body{position:relative;background:var(--page);font-family:"Arimo",Arial,sans-serif;color:var(--text)}

.topbar{position:absolute;left:0;top:0;width:1120px;height:45px;background:var(--topbar);border-top:3px solid var(--blue);border-bottom:3px solid var(--red)}
.topbar-list{position:absolute;right:88px;top:10px;display:flex;gap:38px;list-style:none}
.topbar-item{display:flex;align-items:center;gap:8px;color:#fff;font-size:13px;height:22px}
.topbar-item svg{width:21px;height:21px}

.header{position:absolute;left:0;top:45px;width:1120px;height:110px;background:#fff}
.brand{position:absolute;left:88px;top:28px;display:flex;align-items:center;gap:10px;font-weight:700;font-size:24px;line-height:26px;color:var(--blue);letter-spacing:.3px;text-transform:uppercase}
.brand-mark{width:16px;height:16px;background:var(--red);flex:none}
.brand-name span{display:block}
.nav{position:absolute;left:453px;top:34px;width:582px;height:43px;border-top:1px solid #eee;border-bottom:1px solid #eee;display:flex;list-style:none;font-family:"Open Sans",sans-serif;font-size:14px;color:#6e8aa8}
.nav li{flex:1;display:flex;align-items:center;justify-content:center}
.nav .active{background:var(--blue);color:#fff;border-radius:3px;margin-top:-1px;height:43px;flex:0 0 97px}

.hero{position:absolute;left:0;top:155px;width:1120px;height:199px;background:linear-gradient(90deg,#3f4448 0%,#8d9398 12%,#2f3438 24%,#a7abaf 36%,#4a4f53 48%,#c6c9cb 60%,#5a5f62 72%,#d9dbdc 86%,#8e9396 100%)}
.hero-title{position:absolute;left:96px;top:300px;font-family:"Quicksand",sans-serif;font-weight:300;font-size:32px;letter-spacing:2px;color:#fff}

.intro{position:absolute;left:88px;top:374px;display:flex;align-items:center;gap:8px;font-family:"Quicksand",sans-serif;font-weight:400;font-size:21px;color:#8a8a8a;letter-spacing:1px;text-transform:uppercase}
.intro svg{width:33px;height:33px}

.company{position:absolute;left:133px;top:426px;width:400px;text-align:center}
.company-name{font-family:"Quicksand",sans-serif;font-weight:500;font-size:21px;color:var(--blue);letter-spacing:1.5px;text-transform:uppercase;margin-bottom:10px}
.company p{font-size:14px;color:#6a6a6a;line-height:29px}

.form{position:absolute;left:601px;top:426px;width:433px}
.field{position:absolute;width:212px}
.field label{display:block;font-size:14px;color:#666;height:17px}
.field .input{height:26px;border:1px solid var(--field-border);background:var(--field);font-size:13px;font-style:italic;color:#b5b5b5;padding:4px 5px}
.field.wide{width:433px}
.field.wide .input{height:68px}
.submit{position:absolute;left:325px;top:298px;width:108px;height:39px;background:var(--blue);color:#fff;border-radius:4px;font-size:13px;display:flex;align-items:center;justify-content:center;letter-spacing:.5px}

.offices{position:absolute;left:104px;top:797px;width:342px;display:grid;grid-template-columns:167px 167px;gap:7px 8px;list-style:none}
.office{height:48px;background:linear-gradient(#fafafa,#dedede);border-radius:3px;box-shadow:0 2px 3px rgba(0,0,0,.25);display:flex;align-items:center;justify-content:center;font-family:"Quicksand",sans-serif;font-size:12px;color:#5f7d9c;letter-spacing:.5px}
.office.small{font-size:10px}
.office.active{color:var(--red)}

.map{position:absolute;left:476px;top:792px;width:558px;height:214px;background:linear-gradient(90deg,#e6e2d8 0%,#ddd8cc 60%,#a9c8f0 75%,#9ec2f0 100%)}

.footer{position:absolute;left:0;top:1045px;width:1120px;height:128px;background:var(--footer)}
.footer-col{position:absolute;top:20px}
.footer-title{font-family:"Quicksand",sans-serif;font-weight:400;font-size:15px;color:#9a9a9a;letter-spacing:1px;padding-bottom:3px;border-bottom:1px solid #555;width:175px;text-transform:uppercase}
.footer-links{list-style:none;font-size:11px;color:var(--footer-text);margin-top:12px;line-height:22px}
.footer-links.cols{display:grid;grid-template-columns:74px 74px}
.footer-brand{position:absolute;left:468px;top:36px;width:184px;text-align:center;font-weight:700;font-size:16px;line-height:19px;color:#4a4a4a;text-transform:uppercase;letter-spacing:.5px}
.bottombar{position:absolute;left:0;top:1173px;width:1120px;height:27px;background:var(--footer-bottom);color:#888;font-size:11px;display:flex;align-items:center;justify-content:center}
</style>
</head>
<body>

<header class="topbar">
  <ul class="topbar-list">
    <li class="topbar-item">
      <svg viewBox="0 0 20 20"><circle cx="10" cy="10" r="9.5" fill="#fff"/><path d="M10 4.5a3.5 3.5 0 0 0-3.5 3.5c0 2.6 3.5 7 3.5 7s3.5-4.4 3.5-7A3.5 3.5 0 0 0 10 4.5z" fill="#2a2a2c"/><circle cx="10" cy="8" r="1.3" fill="#fff"/></svg>
      Complete Address Here
    </li>
    <li class="topbar-item">
      <svg viewBox="0 0 20 20"><circle cx="10" cy="10" r="9.5" fill="#fff"/><path d="M5 8c0-1.5 2.2-2.5 5-2.5S15 6.5 15 8l-2 .6-.6-1.4H7.6L7 8.6z" fill="#2a2a2c"/><rect x="6.5" y="9.5" width="7" height="4.5" rx="1" fill="#2a2a2c"/></svg>
      (888) 555-0142
    </li>
    <li class="topbar-item">
      <svg viewBox="0 0 20 20"><circle cx="10" cy="10" r="9.5" fill="#fff"/><rect x="5" y="8" width="10" height="6" rx="1" fill="#2a2a2c"/><rect x="7" y="5" width="6" height="3" fill="#2a2a2c"/></svg>
      (305) 555-0187
    </li>
    <li class="topbar-item">
      <svg viewBox="0 0 20 20"><circle cx="10" cy="10" r="9.5" fill="#fff"/><rect x="5" y="6.5" width="10" height="7" fill="#2a2a2c"/><path d="M5.5 7l4.5 3.5L14.5 7" stroke="#fff" fill="none"/></svg>
      sales@crestlineridgealloys.example
    </li>
  </ul>
</header>

<div class="header">
  <div class="brand"><span class="brand-mark"></span><div class="brand-name"><span>Crestline Ridge</span><span>Alloys</span></div></div>
  <ul class="nav">
    <li>Home</li><li>Products</li><li>Services</li><li>FAQ</li><li>About</li><li class="active">Contact</li>
  </ul>
</div>

<div class="hero" role="img" aria-label="Photograph of rolled stainless steel coils"></div>
<h1 class="hero-title">CONTACT</h1>

<h2 class="intro">
  <svg viewBox="0 0 34 34"><circle cx="17" cy="17" r="15.5" fill="none" stroke="#9a9a9a" stroke-width="1.5"/><path d="M14 10l7 7-7 7" fill="none" stroke="#9a9a9a" stroke-width="1.5"/></svg>
  We look forward to hearing from you!
</h2>

<section class="company">
  <h3 class="company-name">Crestline Ridge Alloys</h3>
  <p>Address: Complete Address Here</p>
  <p>Phone: (888) 555-0142</p>
  <p>Fax: (305) 555-0187</p>
  <p>Email:sales@crestlineridgealloys.example</p>
</section>

<form class="form">
  <div class="field" style="left:0;top:0"><label>Company Name:</label><div class="input">Enter Name</div></div>
  <div class="field" style="left:221px;top:0"><label>Contact Name:</label><div class="input">Enter Email</div></div>
  <div class="field" style="left:0;top:51px"><label>Address 1:</label><div class="input">Enter Text</div></div>
  <div class="field" style="left:221px;top:51px"><label>Address 2:</label><div class="input">Enter Text</div></div>
  <div class="field" style="left:0;top:102px"><label>City:</label><div class="input">Enter Text</div></div>
  <div class="field" style="left:221px;top:102px"><label>Zip Code:</label><div class="input">Enter Text</div></div>
  <div class="field" style="left:0;top:153px"><label>Phone:</label><div class="input">Enter Text</div></div>
  <div class="field" style="left:221px;top:153px"><label>Email</label><div class="input">Enter Text</div></div>
  <div class="field wide" style="left:0;top:205px"><label>Message:</label><div class="input">Enter Your Message</div></div>
  <div class="submit">Submit</div>
</form>

<ul class="offices">
  <li class="office active">Chicago, Illinois</li>
  <li class="office small">Charlotte, North Carolina</li>
  <li class="office">Youngstown, Ohio</li>
  <li class="office small">North Brunswick, New Jersey</li>
  <li class="office">Tampa, Florida</li>
  <li class="office">Houston, Texas</li>
  <li class="office">Atlanta, Georgia</li>
  <li class="office">Los Angeles, CA</li>
</ul>

<div class="map" role="img" aria-label="Street map of Chicago, Illinois office location"></div>

<footer class="footer">
  <div class="footer-col" style="left:87px">
    <div class="footer-title">Crestline</div>
    <ul class="footer-links cols"><li>Home</li><li>FAQ</li><li>Products</li><li>About</li><li>Services</li><li>Contact</li></ul>
  </div>
  <div class="footer-col" style="left:277px">
    <div class="footer-title">Products</div>
    <ul class="footer-links"><li>Shapes</li><li>Materials</li><li>Forms</li></ul>
  </div>
  <div class="footer-brand">Crestline Ridge Alloys</div>
  <div class="footer-col" style="left:668px">
    <div class="footer-title">Location</div>
    <ul class="footer-links"><li style="line-height:16px">Complete Address Here</li><li style="line-height:16px">See Alls Address &gt;&gt;</li></ul>
  </div>
  <div class="footer-col" style="left:860px">
    <div class="footer-title">Contact</div>
    <ul class="footer-links"><li style="line-height:18px">Voice (888) 555-0142</li><li style="line-height:18px">FAX&nbsp;&nbsp; (305) 555-0187</li><li style="line-height:18px">sales@crestlineridgealloys.example</li></ul>
  </div>
</footer>
<div class="bottombar">© 2014 Crestline Ridge Alloys. All Rights Reserved.</div>

</body>
</html>
```